Business Card Design

We offer full auto repair and auto customization from custom wheels to lift kits and drop kits we do it all. I want something that grabs your attention from the start but nothing flashy i am more of a clean crisp modern kinda of guy. I plan on using the design on my business cards and my main business sign .
Updates
I have up loaded an image of my currant business card designed by me , I would like to improve on it
Target Market(s)
20-35 male and female
Industry/Entity Type
Business
Contact Information for Business Card
Corvello Wheel Works
48362 1/2 Parkfield rd
Houston TX, 77070
Manager: Dorian Walsh
P:555-214-7730
F:555-214-7781
Email:Dorian@corvellowheelandgarage.example
website:Corvellowheelandgarage.example
Look and feel

```html
<!DOCTYPE html>
<html lang="en">
<head>
<meta charset="utf-8">
<title>Corvello Wheel Works – Business Card</title>
<link rel="stylesheet" href="https://fonts.googleapis.com/css2?family=Michroma&display=swap">
<style>
  :root {
    --brand-blue: #0d4ea6;
    --brand-blue-deep: #0a3f8c;
    --tread-grey: #5a5a5a;
    --edge-grey: #8a8a8a;
    --card-white: #ffffff;
    --canvas-bg: #e4e6ea;
    --text-on-blue: #ffffff;
  }
  * { box-sizing: border-box; margin: 0; padding: 0; }
  html, body { width: 1200px; height: 900px; overflow: hidden; }
  body {
    background: var(--canvas-bg);
    font-family: "Michroma", "Eurostile", sans-serif;
    display: flex;
    flex-direction: column;
    align-items: center;
    justify-content: center;
    gap: 40px;
  }
  .card {
    position: relative;
    width: 680px;
    height: 388px;
    border-radius: 40px;
    overflow: hidden;
    box-shadow: 0 6px 18px rgba(0,0,0,0.18);
    background: var(--card-white);
  }
  .card-bg { position: absolute; inset: 0; width: 100%; height: 100%; }

  .brand {
    position: absolute;
    display: flex;
    align-items: center;
    gap: 18px;
  }
  .brand-square {
    width: 58px; height: 58px;
    background: var(--tread-grey);
  }
  .brand-name {
    color: var(--brand-blue);
    font-size: 27px;
    line-height: 1.25;
    font-weight: 400;
  }
  .card-front .brand { left: 168px; top: 58px; }
  .card-back .brand { left: 232px; top: 44px; }
  .card-back .brand-name { font-size: 24px; }
  .card-back .brand-square { width: 50px; height: 50px; }

  .identity {
    position: absolute;
    right: 352px;
    top: 262px;
    text-align: right;
    color: var(--text-on-blue);
    font-variant: small-caps;
  }
  .identity .person-name { font-size: 15px; letter-spacing: 1.5px; }
  .identity .person-title { font-size: 11px; letter-spacing: 1.5px; margin-top: 3px; }
  .identity .address { font-size: 11px; letter-spacing: 1.5px; margin-top: 8px; line-height: 1.55; }

  .divider {
    position: absolute;
    left: 342px; top: 262px;
    width: 1px; height: 112px;
    background: var(--text-on-blue);
  }

  .contact-list {
    position: absolute;
    left: 356px; top: 262px;
    list-style: none;
    color: var(--text-on-blue);
    font-size: 11.5px;
    letter-spacing: 1.4px;
  }
  .contact-list li {
    display: flex;
    align-items: center;
    gap: 8px;
    height: 22px;
  }
  .contact-icon { width: 13px; height: 13px; flex: none; }

  .card-back .website {
    position: absolute;
    left: 56px; top: 238px;
    color: var(--text-on-blue);
    font-size: 13px;
    letter-spacing: 2px;
  }
</style>
</head>
<body>

  <section class="card card-front" aria-label="Business card front">
    <svg class="card-bg" viewBox="0 0 680 388" aria-hidden="true">
      <defs>
        <linearGradient id="whiteSheen" x1="0" y1="0" x2="0" y2="1">
          <stop offset="0" stop-color="#ffffff"/>
          <stop offset="1" stop-color="#eeeeee"/>
        </linearGradient>
      </defs>
      <rect width="680" height="388" fill="url(#whiteSheen)"/>
      <path d="M0,120 C180,236 460,252 680,206 L680,388 L0,388 Z" fill="var(--edge-grey)"/>
      <path d="M0,128 C180,252 460,266 680,216 L680,388 L0,388 Z" fill="var(--brand-blue)"/>
    </svg>

    <div class="brand">
      <span class="brand-square"></span>
      <span class="brand-name">Corvello<br>Wheel Works</span>
    </div>

    <div class="identity">
      <p class="person-name">Alden Marsh</p>
      <p class="person-title">Owner / C.E.O</p>
      <p class="address">48362 1/2 Parkfield rd,<br>Houston TX, 77070</p>
    </div>

    <span class="divider"></span>

    <ul class="contact-list">
      <li>
        <svg class="contact-icon" viewBox="0 0 14 14" aria-hidden="true"><circle cx="7" cy="7" r="7" fill="#fff"/><path d="M4.2 3.5l1.6-.3.8 1.9-1 .7a5 5 0 0 0 2.6 2.6l.7-1 1.9.8-.3 1.6c-3.6.2-6.5-2.7-6.3-6.3z" fill="var(--brand-blue)"/></svg>
        555-014-2290
      </li>
      <li>
        <svg class="contact-icon" viewBox="0 0 14 14" aria-hidden="true"><circle cx="7" cy="7" r="7" fill="#fff"/><rect x="5" y="3" width="4" height="8" rx="0.8" fill="var(--brand-blue)"/></svg>
        555-014-7731
      </li>
      <li>
        <svg class="contact-icon" viewBox="0 0 14 14" aria-hidden="true"><circle cx="7" cy="7" r="7" fill="#fff"/><rect x="3.5" y="5.5" width="7" height="4" fill="var(--brand-blue)"/><rect x="5" y="3.5" width="4" height="2" fill="var(--brand-blue)"/></svg>
        555-014-3318
      </li>
      <li>
        <svg class="contact-icon" viewBox="0 0 14 14" aria-hidden="true"><circle cx="7" cy="7" r="7" fill="#fff"/><rect x="3.5" y="4.5" width="7" height="5" fill="var(--brand-blue)"/><path d="M3.5 4.5L7 7.3l3.5-2.8" stroke="#fff" stroke-width="0.8" fill="none"/></svg>
        name@sampledomain.example
      </li>
      <li>
        <svg class="contact-icon" viewBox="0 0 14 14" aria-hidden="true"><circle cx="7" cy="7" r="7" fill="#fff"/><circle cx="7" cy="7" r="3.6" fill="none" stroke="var(--brand-blue)" stroke-width="0.9"/><path d="M3.4 7h7.2M7 3.4c-1.6 2.2-1.6 5 0 7.2M7 3.4c1.6 2.2 1.6 5 0 7.2" stroke="var(--brand-blue)" stroke-width="0.8" fill="none"/></svg>
        www.sampledomain.example
      </li>
    </ul>
  </section>

  <section class="card card-back" aria-label="Business card back">
    <svg class="card-bg" viewBox="0 0 680 388" aria-hidden="true">
      <rect width="680" height="388" fill="url(#whiteSheen)"/>
      <path d="M0,60 C200,200 470,236 680,236 L680,388 L0,388 Z" fill="var(--edge-grey)"/>
      <path d="M0,68 C200,214 470,250 680,248 L680,388 L0,388 Z" fill="var(--brand-blue)"/>
    </svg>

    <div class="brand">
      <span class="brand-square"></span>
      <span class="brand-name">Corvello<br>Wheel Works</span>
    </div>

    <p class="website">www.yourwebsite.example</p>
  </section>

</body>
</html>
```